Fitness business need 3x3 card to promote 6wk boot camp nutrition challenge

Hi, we're looking for someone to make our current card look better and more modern. We want to keep the text the same, but we want a better design. We also want to keep the woman on the front of the card. The card is for both men and women so we want it to feel inclusive and bright. The idea is to make the card look more modern. We want some pops of color. The main feature is to promote the pricing on the back of the card. It would be nice if that continues to look like a coupon or if it stands out with a bright color or background.

Target Market(s)

Men and women looking to get in shape

Industry/Entity Type

Fitness

Font styles to use
Serif
Sans Serif

Colors
3176b5
0255a3
33a6d7
f37122
ec1f27

Requirements
Must have
• front and back, use pic of women provided

```html
<!DOCTYPE html>
<html lang="en">
<head>
<meta charset="utf-8">
<title>Boot Camp Card – Front and Back</title>
<link href="https://fonts.googleapis.com/css2?family=Oswald:wght@500;600&family=Quicksand:wght@600;700&family=Open+Sans:wght@600;700&display=swap" rel="stylesheet">
<style>
  :root{
    --bg:#e6e6e6;
    --navy:#0f3550;
    --blue:#0255a3;
    --mid-blue:#3176b5;
    --sky:#33a6d7;
    --teal-dark:#0f2f3a;
    --teal:#2a6f80;
    --teal-light:#5fa7b3;
    --orange:#f37122;
    --red:#ec1f27;
    --white:#ffffff;
    --ink:#0d2330;
  }
  *{margin:0;padding:0;box-sizing:border-box}
  html,body{width:1200px;height:800px;overflow:hidden;background:var(--bg)}
  .sheet{position:relative;width:1200px;height:800px}
  .card{position:absolute;top:130px;width:540px;height:540px;overflow:hidden;box-shadow:0 6px 14px rgba(0,0,0,.35)}
  .card--front{left:40px;background:linear-gradient(160deg,var(--teal) 0%,var(--teal-dark) 85%)}
  .card--back{left:620px;background:linear-gradient(180deg,#1f5566 0%,#173f4c 40%,#0b1a22 100%)}

  .display{font-family:"Oswald",sans-serif;font-weight:600;text-transform:uppercase;color:var(--orange);line-height:.9;text-shadow:2px 2px 3px rgba(0,0,0,.35)}
  .round{font-family:"Quicksand",sans-serif;font-weight:700;text-transform:uppercase;color:var(--white)}

  /* front */
  .front__panel{position:absolute;left:16px;top:0;width:270px;height:330px;background:linear-gradient(180deg,var(--blue) 0%,rgba(2,85,163,.25) 100%)}
  .front__photo{position:absolute;right:0;top:0;width:330px;height:470px;background:radial-gradient(ellipse at 55% 40%,#c9d3d3 0%,#7e9aa0 35%,#2f5e6a 75%,rgba(15,47,58,0) 100%)}
  .front__title{position:absolute;left:24px;top:28px;font-size:86px;letter-spacing:-1px}
  .front__title span{display:block}
  .challenge{position:absolute;display:flex;align-items:center;gap:6px}
  .challenge__num{font-family:"Oswald",sans-serif;font-weight:600;color:var(--white);line-height:1}
  .challenge__text{line-height:.95}
  .front .challenge{left:32px;top:300px}
  .front .challenge__num{font-size:84px}
  .front .challenge__text{font-size:21px;text-align:center}
  .front__dates{position:absolute;left:34px;top:385px;font-family:"Oswald",sans-serif;font-weight:500;color:var(--white);font-size:31px;line-height:1.1;text-transform:uppercase}
  .front__dates sup{font-size:15px;vertical-align:14px}
  .front__dates .l2{padding-left:12px;display:block}
  .front__band{position:absolute;left:0;right:0;top:477px;height:58px;background:var(--orange);display:flex;align-items:center;justify-content:center;font-family:"Quicksand",sans-serif;font-weight:600;font-size:26px;color:var(--white);letter-spacing:1.5px}
  .logo{position:absolute;display:flex;flex-direction:column;align-items:center;font-family:"Quicksand",sans-serif;font-weight:700;color:var(--white);text-transform:uppercase}
  .logo--front{right:28px;top:30px;width:112px;height:112px;border:5px solid var(--white);border-radius:50%;justify-content:center;font-size:26px;line-height:1.05;text-align:center}

  /* back */
  .back__title{position:absolute;left:46px;top:38px;font-size:70px}
  .back__title .row{display:flex;align-items:center}
  .back .challenge{position:static;margin-left:14px}
  .back .challenge__num{font-size:74px}
  .back .challenge__text{font-size:19px;text-align:center}
  .back__strip{position:absolute;left:0;right:0;top:182px;height:44px;background:var(--orange);display:flex;align-items:center;justify-content:center;font-family:"Oswald",sans-serif;font-weight:500;font-size:28px;color:var(--white);text-transform:uppercase}
  .back__strip b{font-weight:600;color:var(--navy)}
  .back__blurb{position:absolute;left:0;right:0;top:226px;height:62px;background:var(--teal-light);display:flex;align-items:center;justify-content:center;text-align:center;font-family:"Open Sans",sans-serif;font-weight:600;font-size:15px;line-height:1.15;color:var(--ink);padding:0 50px}
  .price{position:absolute;left:46px;top:296px;width:204px;height:204px;border-radius:50%;background:var(--red);border:4px solid var(--white);display:flex;flex-direction:column;align-items:center;justify-content:center;font-family:"Oswald",sans-serif;color:var(--white);line-height:1}
  .price__num{font-size:46px;font-weight:600}
  .price__weeks{font-size:34px;font-weight:600;text-transform:uppercase}
  .price__for{font-family:"Quicksand",sans-serif;font-weight:600;font-size:16px;text-transform:uppercase;margin:2px 0}
  .price__amount{font-size:64px;font-weight:600}
  .price__amount sup{font-size:36px;vertical-align:20px}
  .back__logos{position:absolute;left:280px;top:300px;display:flex;gap:46px}
  .logo--back{position:static;font-size:15px;gap:8px}
  .logo--back i{display:block;width:58px;height:58px;border:3px solid var(--white);border-radius:50%}
  .contact{position:absolute;left:256px;top:402px;width:270px;text-align:center;font-family:"Open Sans",sans-serif;font-weight:700;font-size:13px;line-height:1.35;color:var(--white)}
  .contact__head{text-transform:uppercase;margin-bottom:8px}
</style>
</head>
<body>
<main class="sheet">

  <section class="card card--front front" aria-label="Card front">
    <div class="front__photo" role="img" aria-label="Photo of a woman sitting on the gym floor after a workout"></div>
    <div class="front__panel"></div>
    <h1 class="display front__title"><span>Boot</span><span>Camp</span><span>Title</span></h1>
    <div class="logo logo--front">Your<br>Logo</div>
    <div class="challenge">
      <span class="challenge__num">6</span>
      <span class="round challenge__text">Week Fitness<br>&amp; Nutrition<br>Challenge</span>
    </div>
    <p class="front__dates">October 2<sup>ND</sup> to<span class="l2">November 11<sup>TH</sup></span></p>
    <div class="front__band">www.yourgymurl.com/landingpage</div>
  </section>

  <section class="card card--back back" aria-label="Card back">
    <h2 class="display back__title">
      <span class="row">Boot Camp</span>
      <span class="row">Title
        <span class="challenge">
          <span class="challenge__num">6</span>
          <span class="round challenge__text">Week Fitness<br>&amp; Nutrition<br>Challenge</span>
        </span>
      </span>
    </h2>
    <div class="back__strip"><span><b>No</b> Barbells! <b>No</b> Heavy Weights!</span></div>
    <p class="back__blurb">Burn fat, build muscle &amp; have fun! Tons of classes led by world-class coaches. Personalized nutrition planning, prizes, and more! Sign up Today!</p>
    <div class="price">
      <span class="price__num">6</span>
      <span class="price__weeks">Weeks</span>
      <span class="price__for">For only</span>
      <span class="price__amount"><sup>$</sup>249</span>
    </div>
    <div class="back__logos">
      <div class="logo logo--back"><i></i>Your Logo</div>
      <div class="logo logo--back"><i></i>Your Logo</div>
    </div>
    <div class="contact">
      <p class="contact__head">Learn more at:</p>
      <p>www.yourgymurl.com/landingpage</p>
      <p>(555) 555-5555</p>
      <p>17 Street Name</p>
      <p>City Name, State 10003</p>
    </div>
  </section>

</main>
</body>
</html>
```